Asphalt Paving Specialists Business Cards

Our company is TREVIN ASPHALT. We need a business cards two of our asphalt paving team members. We're asphalt specialists.
I need two made up please. The details on the front of the each business card i would like please is as follows.
Address is 87 Marrowby St, Clontarf, QLD, 4019.

Company Director
Gordon Pelliway
gord@trevinpave.com.au
04 58 736 042
www.trevinpave.com.au

Supervisor
Curtis Vonnegard
curtis@trevinpave.com.au
0462 873 105
www.trevinpave.com.au

We do all aspects of Asphalt Paving. Specific Services include - Driveways, Carparks & sub-divisions. All Roads. Repairs and Maintenance.

We provide free quotes!

I dont have a certain way i want them to look so im open to all designs :)

** I have uploaded our logo for the TREVIN ASPHALT. HOWEVER, CAN YOU PLEASE GET RID OF THE ( PTY LTD )

Thank you
Renata Fulch
TREVIN ASPHALT

Target Market(s)

Home owners and Business Owners

Contact Information for Business Card

Asphalt Paving Specialists. All aspects of Asphalt. Residential, Commercial & Industrial. Based in Brisbane.

Font styles to use
Sans Serif

Colors

Designer to choose colors to be used in the design.

Requirements
Nice to have
• maybe an image of a driveway? or Asphalt?

```html
<!DOCTYPE html>
<html lang="en">
<head>
<meta charset="utf-8">
<title>Trevin Asphalt – Business Cards</title>
<link href="https://fonts.googleapis.com/css2?family=Roboto:wght@400;500;700;900&family=Kaushan+Script&display=swap" rel="stylesheet">
<style>
  :root {
    --backdrop: #5b4633;
    --card-white: #ffffff;
    --asphalt-dark: #1c1c1e;
    --asphalt-mid: #3a3a3c;
    --ink: #161616;
    --brand-blue: #1f9fe0;
    --line-yellow: #e2c31f;
    --road-grey: #6d7277;
    --verge-green: #6f8a4a;
  }
  * { box-sizing: border-box; margin: 0; padding: 0; }
  html, body { width: 900px; height: 1200px; overflow: hidden; }
  body {
    background: var(--backdrop);
    font-family: "Roboto", Arial, sans-serif;
    position: relative;
  }
  .card {
    position: absolute;
    left: 86px;
    width: 734px;
    height: 429px;
    border-radius: 18px;
    overflow: hidden;
    box-shadow: 0 6px 14px rgba(0,0,0,.45);
  }
  /* Back of card */
  .card-back { top: 133px; }
  .card-back .texture {
    position: absolute; inset: 0;
    background: radial-gradient(ellipse at 45% 45%, var(--asphalt-mid), var(--asphalt-dark) 75%);
  }
  .card-back .brand {
    position: absolute;
    left: 0; right: 0; top: 160px;
    display: flex; align-items: center; justify-content: center; gap: 16px;
  }
  .brand-dot {
    width: 34px; height: 34px; border-radius: 50%;
    background: var(--brand-blue);
  }
  .brand-name {
    font-weight: 900;
    font-size: 52px;
    letter-spacing: 1px;
    color: var(--brand-blue);
    line-height: 1;
  }
  .services {
    position: absolute;
    left: 40px; right: 40px; top: 343px;
    text-align: center;
    color: #fff;
    font-size: 15px;
    line-height: 23px;
    text-shadow: 0 1px 2px #000;
  }
  /* Front of card */
  .card-front { top: 633px; background: var(--card-white); }
  .card-front .photo { position: absolute; inset: 0; }
  .card-front .brand {
    position: absolute; left: 40px; top: 70px;
    display: flex; align-items: center; gap: 12px;
  }
  .card-front .brand-name { font-size: 38px; }
  .card-front .brand-dot { width: 26px; height: 26px; }
  .person { position: absolute; left: 44px; top: 183px; }
  .person-name { font-size: 20px; font-weight: 700; color: var(--ink); }
  .person-role { font-size: 15px; font-weight: 500; color: var(--brand-blue); margin-top: 3px; }
  .contacts { position: absolute; left: 44px; top: 247px; list-style: none; }
  .contacts li {
    display: flex; align-items: center; gap: 11px;
    height: 24px; font-size: 15px; color: var(--ink);
  }
  .contacts svg { width: 15px; height: 15px; fill: var(--brand-blue); flex: none; }
  .tagline {
    position: absolute; left: 44px; top: 366px;
    font-family: "Kaushan Script", cursive;
    font-size: 20px; color: var(--ink);
  }
</style>
</head>
<body>

<section class="card card-back">
  <div class="texture" role="img" aria-label="Close-up photo of dark asphalt surface with white and yellow road markings"></div>
  <div class="brand">
    <span class="brand-dot"></span>
    <span class="brand-name">TREVIN ASPHALT</span>
  </div>
  <p class="services">We do all aspects of Asphalt Paving. Specific Services include - Driveways, Carparks<br>&amp; sub-divisions. All Roads. Repairs and Maintenance.</p>
</section>

<section class="card card-front">
  <svg class="photo" viewBox="0 0 734 429" width="734" height="429">
    <defs>
      <linearGradient id="roadPhoto" x1="0" y1="0" x2="0" y2="1">
        <stop offset="0" stop-color="#3b4048"/>
        <stop offset=".45" stop-color="#8a9296"/>
        <stop offset=".65" stop-color="var(--verge-green)"/>
        <stop offset="1" stop-color="var(--road-grey)"/>
      </linearGradient>
    </defs>
    <path role="img" aria-label="Photo of a freshly paved asphalt driveway and a curving road with line markings"
          d="M474 0 C440 60 470 110 520 165 C575 225 545 300 280 429 L734 429 L734 0 Z"
          fill="url(#roadPhoto)"/>
    <path d="M474 0 C440 60 470 110 520 165 C575 225 545 300 280 429"
          fill="none" stroke="#000" stroke-width="8"/>
  </svg>

  <div class="brand">
    <span class="brand-dot"></span>
    <span class="brand-name">TREVIN ASPHALT</span>
  </div>

  <div class="person">
    <p class="person-name">Gordon Pelliway</p>
    <p class="person-role">Company Director</p>
  </div>

  <ul class="contacts">
    <li><svg viewBox="0 0 24 24"><path d="M6.6 10.8a15 15 0 0 0 6.6 6.6l2.2-2.2c.3-.3.7-.4 1-.2 1.1.4 2.3.6 3.6.6.6 0 1 .4 1 1V20c0 .6-.4 1-1 1A17 17 0 0 1 3 4c0-.6.4-1 1-1h3.5c.6 0 1 .4 1 1 0 1.3.2 2.5.6 3.6.1.3 0 .7-.2 1z"/></svg>04 58 736 042</li>
    <li><svg viewBox="0 0 24 24"><path d="M2 5h20v14H2zm2 2v.5l8 5 8-5V7l-8 5z"/></svg>gord@trevinpave.com.au</li>
    <li><svg viewBox="0 0 24 24"><path d="M12 2a10 10 0 1 0 0 20 10 10 0 0 0 0-20zm6.9 6h-3a15 15 0 0 0-1.3-3.6A8 8 0 0 1 18.9 8zM12 4c.8 1.2 1.5 2.5 1.9 4h-3.8c.4-1.5 1.1-2.8 1.9-4zM4.3 14a8 8 0 0 1 0-4h3.4a16 16 0 0 0 0 4zm.8 2h3a15 15 0 0 0 1.3 3.6A8 8 0 0 1 5.1 16zm3-8h-3a8 8 0 0 1 4.3-3.6C8.8 5.5 8.4 6.7 8.1 8zM12 20c-.8-1.2-1.5-2.5-1.9-4h3.8c-.4 1.5-1.1 2.8-1.9 4zm2.3-6H9.7a14 14 0 0 1 0-4h4.6a14 14 0 0 1 0 4zm.3 5.6c.6-1.1 1-2.3 1.3-3.6h3a8 8 0 0 1-4.3 3.6zM16.3 14a16 16 0 0 0 0-4h3.4a8 8 0 0 1 0 4z"/></svg>www.trevinpave.com.au</li>
    <li><svg viewBox="0 0 24 24"><path d="M12 2a7 7 0 0 0-7 7c0 5 7 13 7 13s7-8 7-13a7 7 0 0 0-7-7zm0 9.5a2.5 2.5 0 1 1 0-5 2.5 2.5 0 0 1 0 5z"/></svg>87 Marrowby St, Clontarf, QLD, 4019.</li>
  </ul>

  <p class="tagline">We provide free quotes!</p>
</section>

</body>
</html>
```